Web Portal Design for Keltavo – Subcontractor Verification Platform

Keltavo is a European startup focused on verifying and confirming the identity of subcontractors in the transport and logistics industry to prevent fraud.
The platform’s main functions include:
Company verification – confirming the legitimacy and registration details of transport companies.
Identity verification – authenticating the identity of the person registering the company and associated drivers.
Geo-zone monitoring – a unique mobile feature that allows the creation of geo-fenced areas at loading locations. This enables verification and tracking of who is actually present and authorized to collect the goods.
Safe subcontracting visibility – full transparency of subcontracting chains, ensuring each level of cooperation remains verified and secure.
In short, Keltavo helps build secure subcontractor networks for both shippers and freight forwarders.
I have already created a basic website using Framer, but I am not fully satisfied with the current design and graphic quality. I’m looking for a professional designer who can help improve the UI/UX, visual consistency, and overall aesthetics of the portal to better reflect our innovative and security-focused mission.
Design Style & Colors:
Modern, minimalistic layout
Primary colors: gray, white, and black
Accent color: green (for highlights, buttons, and trust indicators)
Clean typography and intuitive structure
Preference for a professional, tech-oriented look that conveys trust, security, and innovation
The website must definitely include the option to book a demo and provide information about pricing models, which should be easy to edit. There should also be an option to purchase subscriptions directly through the website. There will be three pricing models.
My project should serve as your inspiration, not a template — I’m not expecting it to look identical. We’re looking for something unique and truly “wow.”
Updates
Low design quality
We are looking for a contractor to design and develop a website for the modern application Keltavo, focused on identity verification in the logistics and transport industry. The website will serve as a branding and sales tool, presenting the innovation, security, and professionalism of our solution.
We are not interested in ready-made templates – we expect a fully custom, unique design tailored to the nature of the product and the TSL market.
Keltavo is an advanced platform for verifying the identity of companies, drivers, and subcontractors in logistics. Our goal is to eliminate fraud, theft, and impersonation of legitimate carriers through:
digital identity verification
subcontractor authorisation
creation of trusted company lists
increasing supply chain security
The website should clearly communicate: security, technology, trust, and innovation.
Design Requirements
Style & Design
No ready-made templates
Modern, technology-driven appearance
Premium / corporate-tech aesthetic
Minimalist, clean layout with clear content hierarchy
Colour Scheme
Existing graphics in green tones (we provide our own materials)
Website background: grey or dark (graphite, dark anthracite, deep grey)
Contrasting elements for CTAs and key sections
Industry Focus
Logistics / Transport / Digital Security
Visual identity should evoke:
trust
control
technology
data protection
The website must allow:
easy content editing
independent updating of texts and images without developer involvement
full responsiveness (desktop, tablet, mobile)
fast loading performance
SEO-ready structure
Target Market(s)
Producers
Coding
Number of Pages Required
1 page
Look and feel

```html
<!DOCTYPE html>
<html lang="en">
<head>
<meta charset="utf-8">
<title>Keltavo – Secure Your Transport Subcontractor Network</title>
<link href="https://fonts.googleapis.com/css2?family=Nunito+Sans:wght@400;600;700;800&display=swap" rel="stylesheet">
<style>
:root{
  --green:#1fb457;
  --green-deep:#16a34a;
  --green-soft:rgba(31,180,87,0.14);
  --bg:#1b1e24;
  --surface:#23272f;
  --field:#1f232a;
  --ink:#f2f4f6;
  --muted:#9ca3ae;
  --line:#343a45;
  --chip:#2b303a;
  --footer:#121419;
  --white:#ffffff;
}
*{box-sizing:border-box;margin:0;padding:0}
html,body{width:1200px;height:3763px;overflow:hidden}
body{font-family:"Nunito Sans",Arial,sans-serif;color:var(--ink);background:var(--bg);position:relative}
.abs{position:absolute}
.center{left:0;width:1200px;text-align:center}

.nav{top:0;left:0;width:1200px;height:65px;border-bottom:1px solid var(--line);background:var(--bg)}
.brand{left:76px;top:18px;font-size:25px;font-weight:800}
.nav-links{left:381px;top:22px;display:flex;gap:34px;font-size:15px;color:var(--muted)}
.btn{display:inline-flex;align-items:center;justify-content:center;gap:10px;border-radius:6px;font-weight:700;text-decoration:none}
.btn-outline{border:1px solid var(--line);background:var(--surface);color:var(--ink)}
.btn-green{background:var(--green-deep);color:var(--white)}
.nav .signin{left:972px;top:14px;width:74px;height:36px;font-size:14px}
.nav .demo{left:1063px;top:14px;width:105px;height:36px;font-size:14px}

.chip{display:inline-block;background:var(--chip);border:1px solid var(--line);border-radius:14px;padding:3px 12px;font-size:12px;font-weight:600;color:var(--ink)}
.chip .dot{display:inline-block;width:12px;height:9px;background:var(--green);border-radius:2px;margin-right:6px;vertical-align:-1px}

.hero-title{top:178px;font-size:64px;font-weight:800;line-height:63px;letter-spacing:-0.5px}
.hero-title .accent{color:var(--green)}
.hero-sub{top:334px;left:280px;width:640px;text-align:center;font-size:20px;line-height:34px;color:var(--muted)}
.hero-ctas{top:472px;display:flex;justify-content:center;gap:17px}
.hero-ctas .btn{height:46px;font-size:18px}
.hero-ctas .btn-green{width:245px}
.hero-ctas .btn-outline{width:177px;font-weight:600}

.stats{top:584px;left:111px;width:978px;display:flex}
.stat{flex:1;text-align:center}
.stat b{display:block;font-size:40px;font-weight:800;line-height:46px}
.stat span{font-size:16px;color:var(--muted)}

.sec-title{font-size:38px;font-weight:800}
.sec-sub{font-size:20px;color:var(--muted);line-height:30px}

.features{top:1022px;left:52px;width:1096px;display:flex}
.feature{flex:1;text-align:center;padding:0 37px}
.feature svg{width:32px;height:32px;stroke:var(--green);fill:none;stroke-width:2}
.feature h3{font-size:20px;font-weight:700;margin:28px 0 14px;line-height:29px}
.feature p{font-size:14px;line-height:24px;color:var(--muted)}

.steps{top:1600px;left:69px;width:1062px;display:flex}
.step{flex:1;text-align:center;padding:0 22px}
.step svg{width:48px;height:48px;color:var(--ink)}
.step h3{font-size:21px;font-weight:600;margin:14px 0 16px}
.step p{font-size:16px;line-height:27px;color:var(--muted)}

.plans{top:2149px;left:29px;width:1132px}
.plan{position:absolute;top:0;width:354px;height:497px;border:2px solid var(--line);border-radius:10px;text-align:center;padding:0 26px;background:var(--surface)}
.plan.pro{border-color:var(--green);border-width:3px}
.plan h3{margin-top:30px;font-size:24px;font-weight:600}
.price{margin-top:14px;font-size:38px;font-weight:800}
.price small{font-size:16px;font-weight:400;color:var(--muted)}
.plan .desc{font-size:16px;color:var(--muted);margin-top:2px}
.plan ul{list-style:none;text-align:left;margin-top:26px}
.plan li{display:flex;align-items:center;gap:13px;font-size:14px;height:34px}
.plan li svg{width:20px;height:20px;flex:none}
.plan .btn{position:absolute;left:26px;width:300px;height:46px;font-size:14px}
.plan .btn-outline{background:var(--bg)}
.popular{position:absolute;top:-14px;left:50%;transform:translateX(-50%);background:var(--green-deep);color:var(--white);font-size:12px;font-weight:700;padding:4px 14px;border-radius:14px}

.form-card{left:126px;top:2913px;width:446px;height:562px;border:1px solid var(--line);border-radius:10px;padding:28px 25px;background:var(--surface)}
.form-card h3{font-size:25px;font-weight:600}
.form-card .lead{font-size:13px;color:var(--muted);line-height:20px;margin-top:8px;width:360px}
.field{border:1px solid var(--line);border-radius:6px;height:41px;font-size:14px;color:var(--muted);padding:0 13px;display:flex;align-items:center;margin-top:18px;background:var(--field)}
.row{display:flex;gap:16px}
.row .field{flex:1}
.field.area{height:101px;align-items:flex-start;padding-top:12px}
.form-card .btn{width:396px;height:46px;margin-top:18px;font-size:14px}

.contact{left:623px;top:2962px;width:450px}
.contact h3{font-size:26px;font-weight:600;margin-bottom:22px}
.item{display:flex;gap:18px;align-items:center;margin-bottom:18px}
.ico{width:50px;height:50px;border-radius:8px;background:var(--green-soft);display:flex;align-items:center;justify-content:center}
.ico svg{width:24px;height:24px;stroke:var(--green);fill:none;stroke-width:2}
.item b{display:block;font-size:16px;font-weight:600}
.item span{font-size:16px;color:var(--muted)}
.why{margin:40px 0 0 26px;display:flex;gap:12px}
.why svg{width:26px;height:26px;stroke:var(--green);fill:none;stroke-width:2;flex:none}
.why b{font-size:16px;font-weight:600}
.why p{font-size:13px;color:var(--muted);line-height:25px;margin-top:4px}

.footer{left:0;top:3504px;width:1200px;height:259px;background:var(--footer);color:var(--white);border-top:1px solid var(--line)}
.f-brand{left:34px;top:55px;display:flex;align-items:center;gap:10px;font-size:25px;font-weight:800}
.f-brand i{width:30px;height:30px;background:var(--green-deep);border-radius:6px;display:block}
.f-about{left:34px;top:106px;width:440px;font-size:16px;line-height:25px;color:#d7d9de}
.f-copy{left:34px;top:172px;font-size:13px;color:#b4b8c0}
.f-col{top:50px}
.f-col h4{font-size:16px;font-weight:700;margin-bottom:18px}
.f-col a{display:block;color:#d7d9de;text-decoration:none;font-size:16px;margin-bottom:11px}
</style>
</head>
<body>

<header class="abs nav">
  <div class="abs brand">Keltavo</div>
  <nav class="abs nav-links"><span>Features</span><span>How it Works</span><span>Pricing</span><span>Contact</span></nav>
  <a class="abs btn btn-outline signin">Sign In</a>
  <a class="abs btn btn-green demo">Book Demo</a>
</header>

<section>
  <div class="abs center" style="top:125px"><span class="chip"><span class="dot"></span>Trusted by 10,000+ Transport Companies</span></div>
  <h1 class="abs center hero-title">Secure Your Transport<br><span class="accent">Subcontractor Network</span></h1>
  <p class="abs hero-sub">Prevent fraud and ensure security in your logistics operations with comprehensive verification, identity authentication, and real-time monitoring solutions.</p>
  <div class="abs center hero-ctas">
    <a class="btn btn-green">Book Free Demo <svg width="14" height="14" viewBox="0 0 24 24" fill="none" stroke="#fff" stroke-width="2.5"><path d="M5 12h14M13 6l6 6-6 6"/></svg></a>
    <a class="btn btn-outline">View Pricing</a>
  </div>
  <div class="abs stats">
    <div class="stat"><b>10,000+</b><span>Verified Companies</span></div>
    <div class="stat"><b>99.9%</b><span>Fraud Prevention Rate</span></div>
    <div class="stat"><b>50+</b><span>Countries Covered</span></div>
    <div class="stat"><b>24/7</b><span>Security Monitoring</span></div>
  </div>
</section>

<section id="features">
  <div class="abs center" style="top:756px"><span class="chip">Core Features</span></div>
  <h2 class="abs center sec-title" style="top:792px">Complete Security Solution for Transport &amp; Logistics</h2>
  <p class="abs sec-sub" style="top:864px;left:210px;width:780px;text-align:center">Our comprehensive platform provides end-to-end verification and monitoring to protect your business from fraud and ensure operational security.</p>
  <div class="abs features">
    <div class="feature">
      <svg viewBox="0 0 24 24"><path d="M12 3l7 3v6c0 4.5-3 7.5-7 9-4-1.5-7-4.5-7-9V6z"/></svg>
      <h3>Company Verification</h3>
      <p>Confirm the legitimacy and registration details of transport companies with comprehensive background checks and real-time validation.</p>
    </div>
    <div class="feature">
      <svg viewBox="0 0 24 24"><circle cx="9" cy="8" r="3.5"/><path d="M2.5 20c0-3.6 2.9-6 6.5-6s6.5 2.4 6.5 6"/><path d="M15.5 4.8a3.5 3.5 0 010 6.4M18 14.4c2 .8 3.5 2.8 3.5 5.6"/></svg>
      <h3>Identity Verification</h3>
      <p>Authenticate the identity of company registrants and associated drivers through advanced biometric and document verification.</p>
    </div>
    <div class="feature">
      <svg viewBox="0 0 24 24"><path d="M12 21s-7-6.2-7-11.5a7 7 0 0114 0C19 14.8 12 21 12 21z"/><circle cx="12" cy="9.5" r="2.6"/></svg>
      <h3>Geo-zone Monitoring</h3>
      <p>Create geo-fenced areas at loading locations to verify and track authorized personnel presence for secure goods collection.</p>
    </div>
    <div class="feature">
      <svg viewBox="0 0 24 24"><path d="M2 12s3.6-6.5 10-6.5S22 12 22 12s-3.6 6.5-10 6.5S2 12 2 12z"/><circle cx="12" cy="12" r="3"/></svg>
      <h3>Safe Subcontracting Visibility</h3>
      <p>Full transparency of subcontracting chains, ensuring each level of cooperation remains verified and secure throughout the process.</p>
    </div>
  </div>
</section>

<section id="how">
  <div class="abs center" style="top:1368px"><span class="chip">How It Works</span></div>
  <h2 class="abs center sec-title" style="top:1404px">Simple, Secure, Effective</h2>
  <p class="abs center sec-sub" style="top:1476px">Get started with Keltavo in three easy steps and transform your transport security.</p>
  <div class="abs steps">
    <div class="step">
      <svg viewBox="0 0 48 48"><path d="M4 26l6-6 8 8L42 4l4 5-28 30z" fill="currentColor"/></svg>
      <h3>Register &amp; Verify</h3>
      <p>Sign up your transport company and complete our comprehensive verification process to establish your trusted profile in our network.</p>
    </div>
    <div class="step">
      <svg viewBox="0 0 48 48"><path d="M4 26l6-6 8 8L42 4l4 5-28 30z" fill="currentColor"/></svg>
      <h3>Set Up Monitoring</h3>
      <p>Configure geo-zones at your loading locations and set up identity verification requirements for all authorized personnel and subcontractors.</p>
    </div>
    <div class="step">
      <svg viewBox="0 0 48 48"><path d="M4 26l6-6 8 8L42 4l4 5-28 30z" fill="currentColor"/></svg>
      <h3>Monitor &amp; Secure</h3>
      <p>Real-time monitoring and verification ensure only authorized personnel access your goods, with full transparency across your subcontracting chain.</p>
    </div>
  </div>
</section>

<section id="pricing">
  <div class="abs center" style="top:1934px"><span class="chip">Pricing Plans</span></div>
  <h2 class="abs center sec-title" style="top:1970px">Choose Your Security Level</h2>
  <p class="abs center sec-sub" style="top:2042px">Flexible pricing options to match your business size and security requirements.</p>

  <svg width="0" height="0" style="position:absolute"><defs><symbol id="tick" viewBox="0 0 24 24"><circle cx="12" cy="12" r="9.5" fill="none" stroke="#1fb457" stroke-width="2"/><path d="M8 12.2l2.8 2.8L16.5 9" fill="none" stroke="#1fb457" stroke-width="2"/></symbol></defs></svg>

  <div class="abs plans">
    <div class="plan" style="left:0">
      <h3>Basic</h3>
      <div class="price">€99<small>/month</small></div>
      <p class="desc">Perfect for small transport companies</p>
      <ul>
        <li><svg><use href="#tick"/></svg>Up to 50 verifications/month</li>
        <li><svg><use href="#tick"/></svg>Basic company verification</li>
        <li><svg><use href="#tick"/></svg>Email support</li>
        <li><svg><use href="#tick"/></svg>Standard reporting</li>
        <li><svg><use href="#tick"/></svg>Mobile app access</li>
      </ul>
      <a class="btn btn-outline" style="top:356px">Start Free Trial</a>
    </div>
    <div class="plan pro" style="left:389px">
      <span class="popular">Most Popular</span>
      <h3>Professional</h3>
      <div class="price">€299<small>/month</small></div>
      <p class="desc">Ideal for growing logistics businesses</p>
      <ul>
        <li><svg><use href="#tick"/></svg>Up to 500 verifications/month</li>
        <li><svg><use href="#tick"/></svg>Advanced identity verification</li>
        <li><svg><use href="#tick"/></svg>Geo-zone monitoring</li>
        <li><svg><use href="#tick"/></svg>Priority support</li>
        <li><svg><use href="#tick"/></svg>Advanced analytics</li>
        <li><svg><use href="#tick"/></svg>API access</li>
        <li><svg><use href="#tick"/></svg>Custom integrations</li>
      </ul>
      <a class="btn btn-green" style="top:422px">Start Free Trial</a>
    </div>
    <div class="plan" style="left:778px">
      <h3>Enterprise</h3>
      <div class="price">Custom<small>pricing</small></div>
      <p class="desc">For large-scale operations</p>
      <ul>
        <li><svg><use href="#tick"/></svg>Unlimited verifications</li>
        <li><svg><use href="#tick"/></svg>Full subcontracting visibility</li>
        <li><svg><use href="#tick"/></svg>Dedicated account manager</li>
        <li><svg><use href="#tick"/></svg>24/7 phone support</li>
        <li><svg><use href="#tick"/></svg>Custom reporting</li>
        <li><svg><use href="#tick"/></svg>White-label solution</li>
        <li><svg><use href="#tick"/></svg>SLA guarantee</li>
      </ul>
      <a class="btn btn-outline" style="top:422px">Contact Sales</a>
    </div>
  </div>
</section>

<section id="contact">
  <div class="abs" style="top:2704px;left:0;width:1182px;text-align:center"><span class="chip">Get Started</span></div>
  <h2 class="abs sec-title" style="top:2740px;left:0;width:1182px;text-align:center">Ready to Secure Your Transport Network?</h2>
  <p class="abs sec-sub" style="top:2812px;left:0;width:1182px;text-align:center">Book a personalized demo and see how Keltavo can protect your business from fraud.</p>

  <form class="abs form-card">
    <h3>Book Your Free Demo</h3>
    <p class="lead">Get a personalized demonstration of Keltavo's security features.</p>
    <div class="row"><div class="field">First Name</div><div class="field">Last Name</div></div>
    <div class="field">Company Name</div>
    <div class="field">Email Address</div>
    <div class="field">Phone Number</div>
    <div class="field area">Tell us about your transport security needs...</div>
    <a class="btn btn-green">Schedule Demo <svg width="13" height="13" viewBox="0 0 24 24" fill="none" stroke="#fff" stroke-width="2.5"><path d="M5 12h14M13 6l6 6-6 6"/></svg></a>
  </form>

  <div class="abs contact">
    <h3>Get in Touch</h3>
    <div class="item"><div class="ico"><svg viewBox="0 0 24 24"><path d="M5 3h4l2 5-2.5 1.5a11 11 0 006 6L16 13l5 2v4a2 2 0 01-2 2A17 17 0 013 5a2 2 0 012-2z"/></svg></div><div><b>Phone</b><span>+31 20 555 0187</span></div></div>
    <div class="item"><div class="ico"><svg viewBox="0 0 24 24"><rect x="3" y="5" width="18" height="14" rx="2"/><path d="M3 7l9 6 9-6"/></svg></div><div><b>Email</b><span>hello@keltavo.eu</span></div></div>
    <div class="item"><div class="ico"><svg viewBox="0 0 24 24"><circle cx="12" cy="12" r="9"/><path d="M3 12h18M12 3c2.5 2.5 3.5 5.5 3.5 9S14.5 18.5 12 21c-2.5-2.5-3.5-5.5-3.5-9S9.5 5.5 12 3z"/></svg></div><div><b>Coverage</b><span>50+ European Countries</span></div></div>
    <div class="why">
      <svg viewBox="0 0 24 24"><path d="M12 3l2.7 5.6 6.1.8-4.4 4.2 1.1 6.1L12 16.8l-5.5 2.9 1.1-6.1-4.4-4.2 6.1-.8z"/></svg>
      <div><b>Why Choose Keltavo?</b>
        <p>• 99.9% fraud prevention rate<br>• Real-time verification &amp; monitoring<br>• GDPR compliant &amp; secure<br>• 24/7 European support</p>
      </div>
    </div>
  </div>
</section>

<footer class="abs footer">
  <div class="abs f-brand"><i></i>Keltavo</div>
  <p class="abs f-about">Securing transport and logistics networks across Europe through advanced verification and monitoring solutions.</p>
  <p class="abs f-copy">© 2024 Keltavo. All rights reserved.</p>
  <div class="abs f-col" style="left:618px"><h4>Quick Links</h4><a>Features</a><a>Pricing</a><a>Contact</a><a>About Us</a></div>
  <div class="abs f-col" style="left:910px"><h4>Legal</h4><a>Privacy Policy</a><a>Terms of Service</a><a>GDPR Compliance</a><a>Security</a></div>
</footer>

</body>
</html>
```